TalkBridge - Language Coaching Services

Sleek, innovative, trendy design for Language Coaching business.

TalkBridge is a new UK based company that provides Language Coaching services. We offer highly personalized on-line and face to face language courses. We also impart learning techniques workshops based on the latest neuroscience research for second-language acquisition.

Target Market(s)

Industry/Entity Type

Consulting

Contact Information for Business Card

TalkBridge
ElenaVT@talkbridge-demo.co.uk
TalkBridge-demo.co.uk
London, UK

Font styles to use
Sans Serif

```html
<!DOCTYPE html>
<html lang="en">
<head>
<meta charset="utf-8">
<title>TalkBridge – Business Card</title>
<link rel="stylesheet" href="https://fonts.googleapis.com/css2?family=Montserrat:wght@600;700&family=Open+Sans:wght@400;600&display=swap">
<style>
  :root {
    --backdrop: #3b332e;
    --card: #1b1d20;
    --card-edge: #25282c;
    --silver: #c9cbcd;
    --blue: #1e8fd0;
    --white: #eef0f2;
    --divider: #d8dadc;
  }
  * { box-sizing: border-box; margin: 0; padding: 0; }
  html, body {
    width: 1200px; height: 864px; overflow: hidden;
    background: var(--backdrop);
  }
  .canvas {
    position: relative; width: 1200px; height: 864px;
    display: flex; align-items: center; justify-content: center; gap: 40px;
  }
  .card {
    position: relative; width: 540px; height: 310px;
    background: var(--card);
    border: 1px solid var(--card-edge);
    box-shadow: 0 14px 34px rgba(0,0,0,.45);
    font-family: "Open Sans", Arial, sans-serif;
  }
  .brand {
    display: flex; align-items: center; gap: 12px;
  }
  .brand-mark {
    width: 46px; height: 46px; border-radius: 50%;
    border: 4px solid currentColor;
    flex: none;
  }
  .brand-name {
    font-family: "Montserrat", Arial, sans-serif;
    font-weight: 600; font-size: 32px; letter-spacing: 1px;
    text-transform: uppercase;
  }

  /* front */
  .card-front .brand {
    position: absolute; left: 110px; top: 100px; color: var(--silver);
  }
  .card-front .website {
    position: absolute; left: 110px; top: 186px;
    color: var(--white); font-size: 13px; letter-spacing: 4px;
  }

  /* back */
  .card-back .brand {
    position: absolute; left: 36px; top: 128px; color: var(--blue);
  }
  .card-back .brand-name { font-size: 25px; }
  .card-back .brand-mark { width: 40px; height: 40px; border-width: 3px; }
  .card-back .divider {
    position: absolute; left: 318px; top: 78px;
    width: 1.5px; height: 150px; background: var(--divider);
  }
  .contact {
    position: absolute; left: 340px; top: 90px; color: var(--white);
  }
  .person-name {
    color: var(--blue); font-weight: 700; font-size: 20px;
    font-family: "Open Sans", Arial, sans-serif; text-transform: uppercase;
    line-height: 1.05;
  }
  .person-role {
    font-size: 14px; text-transform: uppercase; margin-bottom: 12px;
  }
  .contact-list { list-style: none; }
  .contact-item {
    display: flex; align-items: center; gap: 8px;
    font-size: 13px; line-height: 22px; white-space: nowrap;
  }
  .contact-item svg { width: 13px; height: 13px; flex: none; }
</style>
</head>
<body>
<main class="canvas">
  <section class="card card-front" aria-label="Business card front">
    <div class="brand">
      <span class="brand-mark"></span>
      <span class="brand-name">TalkBridge</span>
    </div>
    <p class="website">www.talkbridge-demo.co.uk</p>
  </section>

  <section class="card card-back" aria-label="Business card back">
    <div class="brand">
      <span class="brand-name">TalkBridge</span>
      <span class="brand-mark"></span>
    </div>
    <span class="divider"></span>
    <div class="contact">
      <p class="person-name">Elena Torres</p>
      <p class="person-role">President</p>
      <ul class="contact-list">
        <li class="contact-item">
          <svg viewBox="0 0 14 14" aria-hidden="true"><rect x="3.5" y="1" width="7" height="12" rx="1.2" fill="none" stroke="var(--white)" stroke-width="1.4"/><circle cx="7" cy="11" r=".8" fill="var(--white)"/></svg>
          020 7946 0321
        </li>
        <li class="contact-item">
          <svg viewBox="0 0 14 14" aria-hidden="true"><rect x="1" y="3" width="12" height="8.5" fill="var(--white)"/><path d="M1 3 L7 8 L13 3" fill="none" stroke="var(--card)" stroke-width="1.2"/></svg>
          info@talkbridge-demo.co.uk
        </li>
        <li class="contact-item">
          <svg viewBox="0 0 14 14" aria-hidden="true"><circle cx="7" cy="7" r="6" fill="var(--white)"/><path d="M1 7 H13 M7 1 C4 4 4 10 7 13 C10 10 10 4 7 1" fill="none" stroke="var(--card)" stroke-width="1"/></svg>
          talkbridge-demo.co.uk
        </li>
      </ul>
    </div>
  </section>
</main>
</body>
</html>
```